The Duchess of Nestware is an online store specialising in all things for the home Bathroom, Kitchen,

I need a business card designed that is professional and elegant, yet not conservative. We will be wanting to brand the entire business and will have videos made where we will be interacting with the product, testing the products and basically creating an online interactive community for all those people interested in all things to do with the Home and the activities that take place in and around the home.

Target Market(s)

30-65yr old Men and Women who LOVE their Home and see it as their primary place of Happiness, their sanctuary!

Industry/Entity Type

Business

Contact Information for Business Card

www.duchessofnestware.example The Duchess Of Nestware-PO Box 58316, Marlow Flats, Auckland. NEW ZEALAND. info@duchessofnestware.example
Love your Home! Corinne Dale-Petrakou

Font styles to use
Decorative
Script

Colors
9bcb3b
33b8a4
85cae6
b7a5cd
eda3c7
e667a6
d2a4cc
fdf9cf
fee18a

Requirements
Must have
• Attractive colours. Must feel Elegant, yet simple. A font that is rounded without sharp edges. Organic feel to the card, something raw with texture.
Nice to have
• I like the logo deign that I gave in the photos, something feminine, but fun.
Should not have
• I dont like sharp edges, or linear design. I like organic, flowing, fractal type design. Something that looks beautiful in form when you look at it.

```html
<!DOCTYPE html>
<html lang="en">
<head>
<meta charset="utf-8">
<title>The Duchess of Nestware – Business Card</title>
<link rel="stylesheet" href="https://fonts.googleapis.com/css2?family=Questrial&display=swap">
<style>
  :root {
    --page-bg: #2b2b2b;
    --card-white: #ffffff;
    --brand-blue: #3d9fc8;
    --brand-pink: #e5247f;
    --night-blue: #2f5878;
    --wall-blue: #4a7ea6;
    --lamp-glow: #f0a27c;
    --lamp-core: #f7d27a;
    --text-light: #ffffff;
  }
  * { box-sizing: border-box; margin: 0; padding: 0; }
  html, body { width: 1189px; height: 1200px; overflow: hidden; }
  body {
    background: var(--page-bg);
    font-family: "Questrial", "Century Gothic", sans-serif;
    position: relative;
  }
  .card {
    position: absolute;
    left: 171px;
    width: 856px;
    height: 490px;
    border-radius: 84px 24px 84px 14px;
    overflow: hidden;
  }
  .card--front { top: 66px; background: var(--card-white); }
  .card--back { top: 627px; }

  .wordmark { position: absolute; line-height: 1; }
  .wordmark__main { display: block; font-size: 62px; letter-spacing: 0.5px; }
  .wordmark__sub { display: block; font-size: 33px; letter-spacing: 9px; margin-top: 16px; }
  .card--front .wordmark { left: 44px; top: 92px; color: var(--brand-blue); }
  .card--back .wordmark { left: 52px; top: 92px; color: var(--text-light); }

  .holder { position: absolute; left: 44px; top: 280px; }
  .holder__name { font-size: 27px; color: var(--brand-blue); line-height: 1.05; }
  .holder__surname { font-size: 21px; color: var(--brand-pink); line-height: 1.1; }

  .divider {
    position: absolute; left: 44px; top: 345px;
    width: 767px; height: 2px; background: var(--brand-pink);
  }

  .contact-list { position: absolute; left: 44px; top: 366px; list-style: none; }
  .contact-list li {
    display: flex; align-items: center; gap: 10px;
    height: 27.5px; font-size: 20.5px; color: var(--brand-blue);
  }
  .contact-list svg { width: 25px; height: 25px; flex: none; }

  .office { position: absolute; left: 506px; top: 356px; }
  .office__name { font-size: 24px; color: var(--brand-pink); margin-bottom: 10px; }
  .office__line { font-size: 20.5px; color: var(--brand-blue); line-height: 27.5px; }

  .back-photo {
    position: absolute; inset: 0;
    background:
      radial-gradient(ellipse 140px 190px at 640px 300px, rgba(247,210,122,0.95), rgba(240,140,110,0.7) 45%, rgba(240,140,110,0) 100%),
      radial-gradient(ellipse 220px 220px at 620px 170px, rgba(240,162,124,0.75), rgba(240,162,124,0) 100%),
      linear-gradient(100deg, var(--wall-blue) 0%, var(--night-blue) 55%, #3c5f86 100%);
  }

  .social-row {
    position: absolute; left: 99px; top: 348px;
    display: flex; gap: 13px;
  }
  .social-row span {
    width: 35px; height: 35px; border-radius: 50%;
    border: 2px solid var(--text-light);
  }

  .back-url {
    position: absolute; left: 62px; top: 414px;
    font-size: 21.5px; letter-spacing: 1.2px; color: var(--text-light);
  }
</style>
</head>
<body>

<section class="card card--front" aria-label="Business card front">
  <div class="wordmark">
    <span class="wordmark__main">The Duchess</span>
    <span class="wordmark__sub">OF NESTWARE</span>
  </div>

  <div class="holder">
    <p class="holder__name">Corinne Dale</p>
    <p class="holder__surname">Petrakou</p>
  </div>

  <div class="divider"></div>

  <ul class="contact-list">
    <li>
      <svg viewBox="0 0 24 24" aria-hidden="true">
        <circle cx="12" cy="12" r="11" fill="none" stroke="#e5247f" stroke-width="1.6"/>
        <rect x="7" y="10" width="10" height="7" rx="1.5" fill="#e5247f"/>
        <path d="M6 9.5 Q12 5 18 9.5" fill="none" stroke="#e5247f" stroke-width="2" stroke-linecap="round"/>
      </svg>
      64-210555017
    </li>
    <li>
      <svg viewBox="0 0 24 24" aria-hidden="true">
        <circle cx="12" cy="12" r="11" fill="none" stroke="#e5247f" stroke-width="1.6"/>
        <rect x="6.5" y="8" width="11" height="8" rx="1" fill="#e5247f"/>
        <path d="M6.5 8 L12 13 L17.5 8 M6.5 16 L10.5 12 M17.5 16 L13.5 12" fill="none" stroke="#fff" stroke-width="1"/>
      </svg>
      info@duchessofnestware.example
    </li>
    <li>
      <svg viewBox="0 0 24 24" aria-hidden="true">
        <circle cx="12" cy="12" r="11" fill="none" stroke="#e5247f" stroke-width="1.6"/>
        <circle cx="12" cy="12" r="6" fill="none" stroke="#e5247f" stroke-width="1.3"/>
        <ellipse cx="12" cy="12" rx="2.6" ry="6" fill="none" stroke="#e5247f" stroke-width="1.1"/>
        <path d="M6 12 H18 M7 9 H17 M7 15 H17" stroke="#e5247f" stroke-width="1"/>
      </svg>
      www.duchessofnestware.example
    </li>
  </ul>

  <div class="office">
    <p class="office__name">The Duchess Of Nestware</p>
    <p class="office__line">PO Box 58316, Marlow Flats</p>
    <p class="office__line">Auckland. NEW ZEALAND.</p>
  </div>
</section>

<section class="card card--back" aria-label="Business card back">
  <div class="back-photo" role="img" aria-label="Photo of a glowing red lantern casting a heart of warm light onto blue wooden planks"></div>

  <div class="wordmark">
    <span class="wordmark__main">The Duchess</span>
    <span class="wordmark__sub">OF NESTWARE</span>
  </div>

  <div class="social-row" aria-hidden="true">
    <span></span><span></span><span></span><span></span><span></span><span></span>
  </div>

  <p class="back-url">www.duchessofnestware.example</p>
</section>

</body>
</html>
```